Commercial/Corporate Law Firm needs Website Design

Hi guys. I've started up a new law firm and would love your help designing an attractive website. I'll need both design and coding, and to make it easy for us to edit as necessary later, I think it should be built off a Wordpress.org structure.
FIRST IMPRESSIONS
It's very important that the first impression of the website really captures our prospective clients' attention and impresses them. Their first three seconds needs to be good.
I imagine the homepage may be short, with a menu bar and a compelling image, and with a tagline overlaid or underneath (eg. "It's about results.")
The image should be related to our practice areas: eg. IPOs, corporate transactions, or commercial negotiations.
I have previously suggested there could be a skyline image of Sydney or Adelaide. However, because we are based in Adelaide, I don't think Sydney is appropriate - and Adelaide is probably too boring to use.
HOMEPAGE
Being a new firm, we don't have many existing testimonials, and I will be the only lawyer to start with. So we need to focus on the nature of the services we will provide and how my experience can help them. We have an existing logo to use, and I would like the website colour scheme not to clash with that logo (dark blue and white).
After the initial image and tagline there should be a brief introduction to each of the main areas of work, eg. "We specialise in three main areas of practice:"
1. Corporate Transactions and Regulation
2. Business Law and Dispute Resolution
3. Migration Assistance
These should each have an appropriate photo and link to a separate page that briefly describes our services in that area.
Below that there should be a message from me with a photo. Finally, at the bottom, there should be a "Contact Us" section which shows a Google image of our address, contact details, and then our logo with colours inverted.
OTHER PAGES
While we will need some other pages, they should all be fairly simple. I think we will need one page to say "About Us", where I will put information about my experience. I think we will then need one page for each of the 3 areas listed above, which just needs an appropriate image and then text to describe the service. Finally, a "Contact Us" page which I imagine will be the same as the bottom of the homepage.
OTHER DETAILS
For now you can use details from my LinkedIn page to fill out any other text as necessary, or the photo.
Because the logo is square, I would prefer the design of the website also to be rectangular.
Looking forward to seeing your work! Thank you.
Good luck,
Marcus
Target Market(s)
Potential clients:
Businesses with legal issues or disputes
Companies wishing to list on the stock market

```html
<!DOCTYPE html>
<html lang="en">
<head>
<meta charset="utf-8">
<title>Corvell Legal</title>
<link href="https://fonts.googleapis.com/css2?family=Cinzel:wght@600;700&family=Roboto:wght@400;500;700&display=swap" rel="stylesheet">
<style>
:root{
  --navy:#0b3c8c;
  --navy-dark:#08306f;
  --ink:#1d1d1f;
  --muted:#8a8a8a;
  --line:#dcdcdc;
  --paper:#ffffff;
  --mist:#ececee;
  --pin:#d9342b;
}
*{margin:0;padding:0;box-sizing:border-box}
html,body{width:1200px;height:2456px;overflow:hidden}
body{position:relative;background:var(--paper);font-family:'Roboto',sans-serif;color:var(--ink)}
.abs{position:absolute}

/* header */
.topline{left:0;top:0;width:1200px;height:4px;background:var(--navy);z-index:10}
.site-header{left:0;top:4px;width:1200px;height:102px;background:var(--paper)}
.brand-badge{left:98px;top:0;width:194px;height:190px;border-radius:0 0 97px 97px;background:var(--paper);z-index:5;display:flex;flex-direction:column;align-items:center;padding-top:44px}
.brand-square{width:48px;height:48px;background:var(--navy);margin-bottom:10px}
.brand-name{font-family:'Roboto',sans-serif;font-weight:500;color:var(--navy);font-size:20px;letter-spacing:2px;text-align:center;line-height:1.2}
.main-nav{left:380px;top:50px;font-size:14px;font-weight:500;text-transform:uppercase}
.main-nav a{color:var(--ink);text-decoration:none;position:absolute;white-space:nowrap}
.main-nav a.active{color:var(--navy)}
.nav-divider{position:absolute;left:522px;top:-4px;width:1px;height:26px;background:var(--line)}
.nav-call{position:absolute;left:542px;color:var(--navy);font-weight:700;white-space:nowrap}

/* hero */
.hero{left:0;top:106px;width:1200px;height:521px;background:
  radial-gradient(ellipse 260px 300px at 1090px 380px,rgba(214,92,36,.85) 0%,rgba(214,92,36,0) 100%),
  radial-gradient(ellipse 420px 120px at 360px 300px,rgba(245,190,110,.55) 0%,rgba(245,190,110,0) 100%),
  radial-gradient(ellipse 700px 110px at 820px 250px,rgba(230,150,70,.45) 0%,rgba(230,150,70,0) 100%),
  linear-gradient(180deg,#3a5a80 0%,#56708c 22%,#8a6a4e 40%,#3a3438 58%,#1e2230 78%,#111217 100%)}
.hero-title{left:98px;top:458px;font-family:'Cinzel',serif;font-weight:700;font-size:54px;color:#fff;letter-spacing:1px}
.hero-dots{left:98px;top:546px;display:flex;gap:6px}
.hero-dots span{width:11px;height:11px;border-radius:50%;border:1.5px solid #fff}
.hero-dots span.on{background:#fff}

/* section titles */
.section-title{font-family:'Cinzel',serif;font-weight:600;font-size:36px;text-transform:uppercase;color:var(--ink);display:flex;align-items:center;gap:18px;white-space:nowrap}
.section-title em{font-style:normal;color:var(--navy)}
.section-title::before,.section-title::after{content:"";display:block;width:44px;height:1px;background:#bdbdbd}

/* practice cards */
.practice-title{left:0;width:1200px;top:710px;justify-content:center}
.card{top:792px;width:324px;height:400px;border:1px solid #e3e3e3;background:var(--paper)}
.card-photo{width:100%;height:218px}
.card-icon{position:absolute;left:128px;top:184px;width:68px;height:68px;border-radius:50%;background:var(--paper);display:flex;align-items:center;justify-content:center}
.card h3{position:absolute;top:262px;width:100%;text-align:center;font-size:15px;font-weight:500;line-height:25px;text-transform:uppercase;color:var(--ink)}
.card p{position:absolute;top:316px;left:18px;right:18px;text-align:center;font-size:13.5px;line-height:24px;color:var(--muted)}
.btn{display:inline-flex;align-items:center;justify-content:center;height:37px;padding:0 20px;border-radius:19px;background:var(--navy);color:#fff;font-size:13.5px;font-weight:500;text-transform:uppercase;text-decoration:none;white-space:nowrap}
.card .btn{position:absolute;left:101px;bottom:-19px;width:122px}

/* about */
.about{left:0;top:1306px;width:1200px;height:547px;background:
  radial-gradient(ellipse 360px 260px at 1000px 220px,rgba(190,196,208,.5) 0%,rgba(190,196,208,0) 100%),
  linear-gradient(90deg,#ececee 0%,#ededef 50%,#e6e8ec 100%)}
.about-photo{left:116px;top:1397px;width:368px;height:368px;border-radius:50%;background:#1c1f2a;padding:6px}
.about-photo .ring{width:100%;height:100%;border-radius:50%;border:2px solid #d8d8dc;background:
  radial-gradient(circle at 78% 78%,rgba(205,130,55,.7) 0%,rgba(205,130,55,0) 30%),
  radial-gradient(circle at 72% 30%,#6c7a92 0%,rgba(108,122,146,0) 40%),
  linear-gradient(90deg,#3a3d4c 0%,#22252f 50%,#2d3345 100%)}
.about-title{left:524px;top:1404px}
.about-text{left:524px;top:1465px;width:556px;font-size:13px;line-height:31px;color:#8c8c90}
.about .btn{position:absolute;left:524px;top:401px;width:128px}

/* footer */
.map{left:0;top:1853px;width:668px;height:603px;background:
  radial-gradient(ellipse 160px 220px at 490px 260px,rgba(225,225,222,.95) 0%,rgba(225,225,222,0) 100%),
  radial-gradient(ellipse 140px 180px at 420px 520px,rgba(228,228,222,.8) 0%,rgba(228,228,222,0) 100%),
  linear-gradient(100deg,#b9d49a 0%,#c9dcaa 40%,#dfe3cf 60%,#a9c8ea 76%,#9fc0e6 100%)}
.map-pin{position:absolute;left:492px;top:245px}
.contact-panel{left:668px;top:1853px;width:532px;height:603px;background:var(--navy)}
.panel-brand{position:absolute;left:0;width:100%;top:49px;display:flex;flex-direction:column;align-items:center}
.panel-brand .brand-square{background:#fff;width:58px;height:58px;margin-bottom:12px}
.panel-brand .brand-name{color:#fff;font-size:26px;line-height:1.15}
.panel-rule{position:absolute;left:62px;width:408px;height:1px;background:rgba(255,255,255,.16)}
.panel-heading{position:absolute;left:126px;font-size:19px;font-weight:500;color:#fff}
.info-row{position:absolute;left:126px;display:flex;align-items:center;gap:12px;color:#fff;font-size:13px;line-height:21px}
.info-icon{width:42px;height:42px;border-radius:50%;border:1.5px solid #fff;display:flex;align-items:center;justify-content:center;flex:none}
.social{position:absolute;left:126px;top:437px;display:flex;align-items:center;gap:7px;color:#fff}
.social .label{font-size:19px;font-weight:500;margin-right:8px}
.social .dot{width:42px;height:42px;border-radius:50%;border:1.5px solid #fff}
.copyright{position:absolute;left:80px;top:550px;font-size:12px;color:#fff;white-space:nowrap}
</style>
</head>
<body>

<div class="abs topline"></div>
<header class="abs site-header">
  <nav class="abs main-nav">
    <a class="active" href="#" style="left:0">Home</a>
    <a href="#" style="left:90px">About</a>
    <a href="#" style="left:183px">Practice Areas</a>
    <a href="#" style="left:348px">News</a>
    <a href="#" style="left:435px">Contact</a>
    <span class="nav-divider"></span>
    <span class="nav-call">Call Us : 1 800 555 0142</span>
  </nav>
</header>
<div class="abs brand-badge">
  <div class="brand-square"></div>
  <div class="brand-name">CORVELL<br>LEGAL</div>
</div>

<section class="abs hero" role="img" aria-label="Night city skyline with a lit harbour bridge over the water"></section>
<h1 class="abs hero-title">WE GET RESULTS</h1>
<div class="abs hero-dots"><span class="on"></span><span></span><span></span><span></span><span></span></div>

<h2 class="abs section-title practice-title">Practice <em>Areas</em></h2>

<article class="abs card" style="left:98px">
  <div class="card-photo" role="img" aria-label="Hands passing banknotes across a desk with documents" style="background:radial-gradient(ellipse 120px 70px at 160px 110px,rgba(196,170,140,.8) 0%,rgba(196,170,140,0) 100%),linear-gradient(135deg,#4a4e58 0%,#c9ced6 35%,#eceef1 70%,#d4d8de 100%)"></div>
  <div class="card-icon"><svg width="40" height="40" viewBox="0 0 44 44" fill="none" stroke="#0b3c8c" stroke-width="2"><rect x="8" y="14" width="28" height="16" rx="2"/><circle cx="22" cy="22" r="4"/><path d="M6 10h10M28 34h10"/></svg></div>
  <h3>Corporate Transactions<br>and Regulation</h3>
  <p>Sed ut perspiciatis unde omnis iste natus error siptatem accusantium doloremque</p>
  <a class="btn" href="#">Read More</a>
</article>

<article class="abs card" style="left:439px">
  <div class="card-photo" role="img" aria-label="Businessman in a suit signing a contract" style="background:radial-gradient(ellipse 90px 120px at 210px 60px,#2c3c64 0%,rgba(44,60,100,0) 100%),linear-gradient(135deg,#dfe6f0 0%,#b4c2d8 45%,#eef0f4 75%,#c4ccd8 100%)"></div>
  <div class="card-icon"><svg width="40" height="40" viewBox="0 0 44 44" fill="none" stroke="#0b3c8c" stroke-width="2"><circle cx="12" cy="12" r="4"/><circle cx="32" cy="12" r="4"/><path d="M6 36V22h12v14M26 36V22h12v14"/><circle cx="22" cy="22" r="5"/></svg></div>
  <h3>Business Law<br>and Dispute Resolution</h3>
  <p>Sed ut perspiciatis unde omnis iste natus error siptatem accusantium doloremque</p>
  <a class="btn" href="#">Read More</a>
</article>

<article class="abs card" style="left:778px">
  <div class="card-photo" role="img" aria-label="Hands typing on a laptop keyboard" style="background:radial-gradient(ellipse 110px 90px at 230px 150px,#3a3c48 0%,rgba(58,60,72,0) 100%),linear-gradient(135deg,#5a5c6a 0%,#b8bcc6 40%,#d8dbe2 65%,#7a7e8c 100%)"></div>
  <div class="card-icon"><svg width="40" height="40" viewBox="0 0 44 44" fill="none" stroke="#0b3c8c" stroke-width="2"><rect x="10" y="8" width="24" height="20" rx="1"/><circle cx="22" cy="18" r="5"/><path d="M4 34h36l-4-6H8z"/></svg></div>
  <h3>Migration Assistance</h3>
  <p style="top:291px">Sed ut perspiciaoccaecat cupidatat non prtis unde omnis iste natus error siptatem accu-santiecat cupidatat non prmque</p>
  <a class="btn" href="#">Read More</a>
</article>

<section class="abs about">
  <a class="btn" href="#">Read More</a>
</section>
<div class="abs about-photo"><div class="ring" role="img" aria-label="Portrait of the principal lawyer in a dark suit and red tie against a night city"></div></div>
<h2 class="abs section-title about-title">About <em>Me</em></h2>
<p class="abs about-text">Sed ut perspiciatis unde omnis iste natus error sit voluptatem accusantium doloremque laudan-tium, totam rem aperiam, eaque ipsa quae ab illo inventore veritatis et quasi architecto beatae vitae dicta sunt explicabo. Nemo enim ipsam voluptatem quia voluptas sit aspernatur aut odit aut fugit, sed quia coa sunt explicabemo enim ipsam voluptatem quia voluptas sit aspernatur aut odit aut fugit, sednsequuntur magni dolores eos qui ratione voluptatem sequi nesciunt quisquam est, qui dolorem ipsum quia dolor sit amet, consectetur, adipisci velit, sed quia non numquam eius modi tempora incidunt ut labore et dolore magnam aliquam quaerat voluptatem</p>

<div class="abs map" role="img" aria-label="Road map of the coastal region around the office with a location pin">
  <svg class="map-pin" width="28" height="38" viewBox="0 0 28 38"><path d="M14 1C6.8 1 1 6.6 1 13.6 1 23 14 37 14 37s13-14 13-23.4C27 6.6 21.2 1 14 1z" fill="var(--pin)"/><circle cx="14" cy="13.5" r="5" fill="#fff"/></svg>
</div>

<footer class="abs contact-panel">
  <div class="panel-brand">
    <div class="brand-square"></div>
    <div class="brand-name">CORVELL<br>LEGAL</div>
  </div>
  <div class="panel-rule" style="top:190px"></div>
  <div class="panel-heading" style="top:222px">Address Info :</div>
  <div class="info-row" style="top:267px">
    <span class="info-icon"><svg width="20" height="18" viewBox="0 0 20 18" fill="#fff"><path d="M10 1 1 9h3v8h4v-5h4v5h4V9h3z"/></svg></span>
    <span>13,Excepteur sint occaecat cupidatatno<br>proident sunt inculpa..</span>
  </div>
  <div class="info-row" style="top:323px">
    <span class="info-icon"><svg width="18" height="18" viewBox="0 0 24 24" fill="#fff"><path d="M6.6 10.8a15 15 0 0 0 6.6 6.6l2.2-2.2a1 1 0 0 1 1-.25 11.4 11.4 0 0 0 3.6.57 1 1 0 0 1 1 1V20a1 1 0 0 1-1 1A17 17 0 0 1 3 4a1 1 0 0 1 1-1h3.5a1 1 0 0 1 1 1c0 1.25.2 2.45.57 3.57a1 1 0 0 1-.25 1z"/></svg></span>
    <span>Phone : 1 800 555 0142</span>
  </div>
  <div class="info-row" style="top:379px">
    <span class="info-icon"><svg width="20" height="15" viewBox="0 0 20 15" fill="#fff"><path d="M0 0h20v2l-10 6L0 2z"/><path d="M0 4l10 6 10-6v11H0z"/></svg></span>
    <span>Email : info@corvell-legal.com</span>
  </div>
  <div class="social"><span class="label">Follow us :</span><span class="dot"></span><span class="dot"></span><span class="dot"></span></div>
  <div class="panel-rule" style="top:513px"></div>
  <div class="copyright">© copyright 2018 Corvell Legal.All Rights Reserved &nbsp;|&nbsp; Privacy policy</div>
</footer>

</body>
</html>
```